Body corporate management needs business principle flyer design

We need a one page A4 flyer design for our business principles.
We manage body corporates and strata properties.
TenuraKeep is a new initiative for our company. Its a label that we have given to our principles of business that drive our people, systems and processes to give assurance to our clients that every detail matters.
We would like to be able to include this design in future brochure so we are after 1 x portrait and 1 x landscape.
The design needs to portray professionalism.
We would like to see designs that use the colour red. (see attached logo).

Target Market(s)

Professionals

Industry/Entity Type

Business

Font styles to use
Sans Serif

Requirements
Must have
• TenuraKeep logo, provide the design file and as pdf
Nice to have
• the use of the colour red from the logo

```html
<!DOCTYPE html>
<html lang="en">
<head>
<meta charset="utf-8">
<title>TenuraKeep – Principles of Business</title>
<link href="https://fonts.googleapis.com/css2?family=Open+Sans:wght@400;600&family=Arimo:wght@400;700&display=swap" rel="stylesheet">
<style>
  :root {
    --red: #e63a2e;
    --ink: #1c1c1c;
    --body: #2b2b2b;
    --dark: #1e1e1e;
    --paper: #ffffff;
  }
  * { box-sizing: border-box; margin: 0; padding: 0; }
  html, body { width: 857px; height: 1200px; overflow: hidden; background: var(--paper); }
  .flyer { position: relative; width: 857px; height: 1200px; background: var(--paper); font-family: "Open Sans", Arial, sans-serif; color: var(--body); }

  .hero { position: absolute; left: 0; top: 0; width: 857px; height: 228px; background: var(--dark); overflow: hidden; }
  .hero-visual { position: absolute; inset: 0; background:
      radial-gradient(circle at 36% 38%, #6a6a6a 0%, #3c3c3c 18%, rgba(30,30,30,0) 42%),
      radial-gradient(circle at 62% 70%, #555 0%, rgba(30,30,30,0) 25%),
      linear-gradient(90deg, #262626 0%, #2e2e2e 50%, #1a1a1a 100%); }
  .brand-name { position: absolute; right: 66px; top: 92px; font-family: "Open Sans", Arial, sans-serif; font-weight: 600; font-size: 32px; line-height: 1; color: var(--red); }
  .hero-title { position: absolute; right: 66px; top: 150px; color: #fff; font-family: "Arimo", Arial, sans-serif; }
  .hero-title h1 { font-size: 31px; font-weight: 700; line-height: 1; letter-spacing: -0.5px; }
  .hero-title p { font-size: 16.5px; font-weight: 700; margin-top: 4px; }

  .intro { position: absolute; left: 90px; top: 267px; width: 680px; font-family: "Arimo", Arial, sans-serif; font-weight: 700; font-size: 17.5px; line-height: 22px; color: var(--ink); }

  .principle { position: absolute; }
  .principle h2 { display: flex; align-items: center; gap: 14px; font-family: "Open Sans", Arial, sans-serif; font-weight: 600; font-size: 15.5px; color: var(--red); height: 34px; }
  .principle h2 svg { width: 34px; height: 34px; flex: none; fill: var(--red); }
  .principle h2 svg .line { fill: none; stroke: var(--red); stroke-width: 3; }
  .principle h2 svg .cut { fill: #fff; }
  .principle p { position: absolute; font-size: 12.1px; line-height: 14.7px; color: var(--body); }
  .col-left { left: 90px; width: 310px; }
  .col-left p { left: 0; width: 296px; }
  .col-right { left: 468px; width: 330px; }
  .col-right p { left: 0; width: 310px; font-size: 12.8px; line-height: 16px; }

  .contact-band { position: absolute; left: 335px; top: 1119px; width: 522px; height: 81px; background: var(--red); clip-path: polygon(12px 0, 100% 0, 100% 100%, 0 100%); color: #fff; font-family: "Arimo", Arial, sans-serif; font-size: 13px; line-height: 16px; text-align: center; padding-top: 13px; padding-left: 20px; }
</style>
</head>
<body>
<div class="flyer">
  <header class="hero">
    <div class="hero-visual" role="img" aria-label="Photo of a fingertip touching a glowing circular digital interface on a dark background"></div>
    <div class="brand-name">TenuraKeep</div>
    <div class="hero-title">
      <h1>TenuraKeep</h1>
      <p>Principles of Business</p>
    </div>
  </header>

  <h2 class="intro">TenuraKeep Is Our Principles Of Business That Drive Our People, Systems And Processes To Give Assurance To Our Clients That Every Detail Matters.</h2>

  <section class="principle col-left" style="top:352px">
    <h2><svg viewBox="0 0 34 34"><path d="M3 13h6l14-8v24L9 21H3z"/><rect x="7" y="21" width="5" height="9"/><rect x="25" y="14" width="5" height="6"/></svg>Client Experience</h2>
    <p style="top:48px">Our promise is to pursue excellence and to continually deliver a solutions based service. We achieve this through active engagement, open channels of communication and a serviced led team with the dedicated resources to listen, engage and implement.</p>
  </section>

  <section class="principle col-left" style="top:491px">
    <h2><svg viewBox="0 0 34 34"><path d="M2 12l8-6 8 6 8-6 6 6-12 14-4-3-4 3-4-4z"/></svg>Loyalty</h2>
    <p style="top:44px">We seek to develop a life-time relationship with our clients, building trust by acting with integrity, honesty and courtesy. We achieve this due to our expert approach to strata management and providing a responsive service to our clients.</p>
  </section>

  <section class="principle col-left" style="top:616px">
    <h2><svg viewBox="0 0 34 34"><path d="M26 3l5 5-12 12-6 1 1-6z"/><path d="M12 21l-5 8-4 2 2-4z"/></svg>Education and Guidance</h2>
    <p style="top:44px">We endeavor to always be proactive in client education and guidance. This is achieved by our internal and external communications, comprehensive training programs and cross-departmental collaboration of knowledge sharing.</p>
  </section>

  <section class="principle col-left" style="top:768px">
    <h2><svg viewBox="0 0 34 34"><path d="M17 2L2 10h30z"/><rect x="3" y="12" width="28" height="3"/><rect x="6" y="17" width="4" height="10"/><rect x="15" y="17" width="4" height="10"/><rect x="24" y="17" width="4" height="10"/><rect x="2" y="28" width="30" height="4"/></svg>Compliance &amp; Governance</h2>
    <p style="top:44px">We engage and own a position of ‘every detail matters’. We give due diligence to the relevant state and national legislations with which we, our clients and our stakeholders must comply. We regulate and achieve this through a robust system of internal processes and protocols which structure and confirm our deliverables are in line with regulations.</p>
  </section>

  <section class="principle col-left" style="top:934px">
    <h2><svg viewBox="0 0 34 34"><circle cx="13" cy="13" r="8"/><circle cx="26" cy="24" r="5"/><circle class="cut" cx="13" cy="13" r="3"/><circle class="cut" cx="26" cy="24" r="2"/></svg>Systems and processes</h2>
    <p style="top:44px">We strive to be the best in our field, by implementing efficiencies without compromising service quality, accuracy or compliance. We continually seek to achieve this by reviewing, updating and adopting continuous improvement strategies, systems and quality processes that deliver outcomes.</p>
  </section>

  <section class="principle col-right" style="top:353px">
    <h2><svg viewBox="0 0 34 34"><circle class="line" cx="15" cy="18" r="12"/><path class="line" d="M9 17l6 6 15-17"/></svg>Quality &amp; Commitment</h2>
    <p style="top:46px">We invest in the recruitment and retention of a quality and diverse team of experienced professionals with a strong focus on continual professional development.  As committed and skilled individuals, we actively promote the cross-departmental collaboration with one another to deliver a well rounded offering.</p>
  </section>

  <section class="principle col-right" style="top:516px">
    <h2><svg viewBox="0 0 34 34"><path d="M3 3h5l5 20h17v3H11L6 6H3z"/><rect x="15" y="9" width="13" height="11" transform="rotate(-12 21 14)"/><circle cx="13" cy="29" r="3"/></svg>Delivery</h2>
    <p style="top:64px">We empower our teams to deliver an outstanding client service and to be accountable for their actions. We will make sure every detail matters, provide valuable insight and supply information in a clear and timely manner.</p>
  </section>

  <section class="principle col-right" style="top:666px">
    <h2><svg viewBox="0 0 34 34"><path d="M8 4h18l6 9-15 18L2 13z"/></svg>Integrity</h2>
    <p style="top:61px">Our approach to strata management is bound by honesty and a strong set of moral principles. We act in our clients’ best interests with diligence and transparency for understanding and accountability.</p>
  </section>

  <section class="principle col-right" style="top:812px">
    <h2><svg viewBox="0 0 34 34"><path d="M2 2h2v28h28v2H2z"/><rect x="7" y="20" width="5" height="9"/><rect x="14" y="15" width="5" height="14"/><rect x="21" y="18" width="5" height="11"/><path d="M6 16l8-7 6 5 9-10 2 2-11 12-6-5-7 6z"/></svg>Continuous Improvement</h2>
    <p style="top:60px">Our goal is to continually evolve to better our offering and to be adaptable and responsive to change. Our infrastructure supports us to continually mould into the business that is right for our clients.</p>
  </section>

  <section class="principle col-right" style="top:958px">
    <h2><svg viewBox="0 0 34 34"><path d="M3 4h20v26H3z"/><rect class="cut" x="7" y="10" width="12" height="2"/><rect class="cut" x="7" y="15" width="12" height="2"/><rect class="cut" x="7" y="20" width="8" height="2"/><path d="M30 8l3 3-12 13-4 1 1-4z"/></svg>Ethical Stance</h2>
    <p style="top:60px">We aim to create a community of ethical business relationships where we contribute our values and services to give our clients outstanding reassurance of our abilities.</p>
  </section>

  <footer class="contact-band">
    Contact us<br>
    Tel: 1300 555 0142&nbsp;&nbsp;Fax&nbsp;&nbsp;1300 555 0143<br>
    Website :www.tenurakeep.com&nbsp;&nbsp;&nbsp;Email: info@tenurakeep.co
  </footer>
</div>
</body>
</html>
```